Willow of Meadow Uniform Label Redesign

To refine our current product label designs into one, simple, modern, crisp, general look that can be adapted to all our all Natural Skin Care and Wellness products. I am inspired by the elegant versatility of products like Lumavel Botanic Beauty or Tarn Beauty label schemes. We no longer want labels that indicate scent or ingredients. We have two primary colors that we want to maintain (#096CA3 and #DEE33F), and are willing to entertain subtle additions of others, other than black. Our labels will be printed on white or clear material. We use mainly Cosmo or Boston Round container shapes, plus flat top, smooth, round jars. Maybe a faded watermark highlight the "natural" or "beautiful" side of our products. we need to convey confidence, while remaining simple. We currently use the Advantage font. Maybe Century Gothic may work. Something similar that is easy on the eyes. Maybe vertical main text? We are willing to entertain a lot of ideas. These designs will offer ideas into our eventual Website (www.willowofmeadow-example.com) redesign.

Target Market(s)

Those who are familiar with the power of natural, plant based skin care and wellness products

Industry/Entity Type

Natural Skin Care and Wellness

Font styles to use
Sans Serif
Other font styles liked:
• Century Gothic, Advantage, or similar that is easy on the eyes

Colors
0054AA
0677BA
7BADD7
CADEEF
E8F1F8
59FF00
82FF00
B8FF75
E3FFCB
F4FFEA

Requirements
Must have
• "Clean Lines"; These colors: (#096CA3 and #DEE33F)
Nice to have
• MAYBE vertical main text or a watermark image

```html
<!DOCTYPE html>
<html lang="en">
<head>
<meta charset="utf-8">
<title>Willow of Meadow – Sugar Body Polish Label</title>
<link href="https://fonts.googleapis.com/css2?family=Roboto:wght@400;500;700&family=EB+Garamond:wght@400&display=swap" rel="stylesheet">
<style>
  :root {
    --brand-blue: #096CA3;
    --brand-green: #DEE33F;
    --label-white: #ffffff;
    --page-bg: #f8f8f8;
    --body-text: #3f3f3f;
    --heading-text: #333333;
    --muted-text: #555555;
    --petal-pink: #e85aa8;
    --petal-light: #f39bcd;
  }
  * { margin: 0; padding: 0; box-sizing: border-box; }
  html, body {
    width: 1200px; height: 491px; overflow: hidden;
    background: var(--page-bg);
  }
  .canvas { position: relative; width: 1200px; height: 491px; }
  .label {
    position: absolute; left: 119px; top: 10px;
    width: 962px; height: 470px;
    background: var(--label-white);
    overflow: hidden;
    font-family: "Roboto", Arial, sans-serif;
  }
  .top-band {
    position: absolute; left: 0; top: 0; width: 100%; height: 182px;
    background: var(--brand-green);
  }
  .bottom-band {
    position: absolute; left: 0; bottom: 0; width: 100%; height: 14px;
    background: var(--brand-green);
  }
  .brand-name {
    position: absolute; left: 0; width: 100%; top: 40px;
    text-align: center;
    font-size: 36px; font-weight: 400; line-height: 44px;
    color: var(--brand-blue);
  }
  .tagline {
    position: absolute; left: 0; width: 100%; top: 95px;
    text-align: center;
    font-size: 16px; line-height: 20px;
    color: var(--brand-blue);
  }
  .flower-photo {
    position: absolute; left: 385px; top: 128px;
    width: 190px; height: 54px;
    border-radius: 50% 50% 0 0 / 100% 100% 0 0;
    background: radial-gradient(ellipse at 50% 40%, var(--petal-light), var(--petal-pink) 75%);
  }
  .product-title {
    position: absolute; left: 0; width: 100%; top: 198px;
    text-align: center;
    font-size: 44px; font-weight: 700; line-height: 38px;
    color: var(--brand-blue);
  }
  .title-rule {
    position: absolute; left: 285px; top: 288px;
    width: 392px; height: 14px;
    background: var(--brand-blue);
  }
  .description {
    position: absolute; left: 0; width: 100%; top: 320px;
    text-align: center;
    font-family: "EB Garamond", Georgia, serif;
    font-size: 23px; line-height: 24px;
    color: var(--muted-text);
  }
  .net-weight {
    position: absolute; left: 0; width: 100%; top: 412px;
    text-align: center;
    font-size: 19px; line-height: 24px;
    color: var(--muted-text);
  }
  .info-column {
    position: absolute; width: 230px;
    font-size: 15.5px; line-height: 21px;
    color: var(--body-text);
  }
  .info-column h2 {
    font-size: 16px; font-weight: 500; line-height: 21px;
    color: var(--heading-text);
  }
  .how-to-use { left: 38px; top: 196px; }
  .ingredients { left: 724px; top: 199px; }
</style>
</head>
<body>
<div class="canvas">
  <div class="label">
    <div class="top-band"></div>
    <div class="brand-name">Willow of Meadow</div>
    <div class="tagline">pure. gentle. lasting.</div>
    <div class="flower-photo" role="img" aria-label="Photo of pink rose geranium petals"></div>

    <section class="info-column how-to-use">
      <h2>How to Use</h2>
      <p>Lorem ipsum dolor sit amet,<br>consectetur adipiscing elit,<br>sed do eiusmod tempor<br>incididunt ut labore et dolore<br>magna aliqua. Ut enim ad<br>minim veniam, quis nostrud<br>exercitation ullamco laboris<br>nisi ut aliquip ex ea commodo<br>nsequat. Duis aute irure dolor<br>in reprehenderit in voluptate</p>
    </section>

    <h1 class="product-title">SUGAR BODY<br>POLISH</h1>
    <div class="title-rule"></div>
    <p class="description">exfoliates your skin &amp;<br>remove outer layer of old skin cells<br>with Rose Geranium &amp; Shea</p>
    <p class="net-weight">250 gr</p>

    <section class="info-column ingredients">
      <h2>Ingredients</h2>
      <p>Lorem ipsum dolor sit amet,<br>consectetur adipiscing elit,<br>sed do eiusmod tempor<br>incididunt ut labore et dolore<br>magna aliqua. Ut enim ad<br>minim veniam, quis nostrud<br>exercitation ullamco laboris<br>nisi ut aliquip ex ea commodo<br>nsequat. Duis aute irure dolor<br>in reprehenderit in voluptate</p>
    </section>

    <div class="bottom-band"></div>
  </div>
</div>
</body>
</html>
```